Full 10+ Page Online Learning eBook Design - NOT just the cover :)

We currently have an eBook within the online learning space which is geared towards a consumer audience (hobbyists, interests), but we have a new 2.0 version which is geared towards professionals (certifications, training, continuing ed, career-oriented). We need a new design and need the words/copy put into the eBook, but want to keep the look and feel of the original (open to variations in design). File is attached, along with various logo options.

Target Market(s)

Professionals

Industry/Entity Type

Learning

Font styles to use
Sans Serif

Colors
33a6d7
acd036
919191

Requirements
Must have
• Must follow a very similar look a feel of the original file. We use a lot of fonts like Raleway, Gotham, Helvetica Neue, Gil Sans, DIN - anything modern looking. We also use a lot of grayish hexagons in our corporate design. Feel free to check out brightlanternworks.example to get a better sense.
Nice to have
• Include some professionally oriented icons / photos
Should not have
• No cartoonish graphics or imagery

```html
<!DOCTYPE html>
<html lang="en">
<head>
<meta charset="utf-8">
<title>Turning Training Into Growth 2.0 – eBook Pages</title>
<link rel="stylesheet" href="https://fonts.googleapis.com/css2?family=Oswald:wght@400;500&family=Raleway:wght@400;500;600;700&display=swap">
<style>
  :root {
    --brand-blue: #33a6d7;
    --brand-blue-deep: #1f86c0;
    --brand-blue-light: #6cc3ea;
    --brand-green: #acd036;
    --brand-gray: #919191;
    --ink: #2f3a44;
    --paper: #ffffff;
    --stage: #ffffff;
  }
  * { box-sizing: border-box; margin: 0; padding: 0; }
  html, body { width: 889px; height: 1200px; overflow: hidden; background: var(--stage); }
  body { position: relative; font-family: "Raleway", "Helvetica Neue", Arial, sans-serif; color: var(--ink); }

  .page { position: absolute; width: 285px; height: 445px; overflow: hidden; box-shadow: 0 2px 8px rgba(0,0,0,.18); }
  .page--front { left: 152px; top: 26px; background: var(--paper); }
  .page--back  { left: 470px; top: 26px; }
  .page--preface { left: 152px; top: 606px; }
  .page--contents { left: 470px; top: 606px; }

  .page-label { position: absolute; width: 285px; text-align: center; font-size: 17px; font-weight: 500; letter-spacing: .5px; color: #444; }
  .page-label--front { left: 152px; top: 490px; }
  .page-label--back { left: 470px; top: 490px; }
  .page-label--preface { left: 152px; top: 1070px; }
  .page-label--contents { left: 470px; top: 1070px; }

  /* Publisher name, plain text */
  .publisher { position: absolute; left: 0; width: 100%; text-align: center; font-family: "Raleway", sans-serif; font-weight: 600; font-size: 9px; }

  /* Front page */
  .cover-photo { position: absolute; left: 0; top: 0; width: 285px; height: 200px; background: linear-gradient(160deg, #e9eef2 0%, #b8c3cc 45%, #7d8c99 100%); }
  .cover-kicker { position: absolute; top: 66px; left: 0; width: 100%; text-align: center; font-family: "Oswald", sans-serif; font-size: 15px; letter-spacing: 1.5px; color: var(--ink); background: rgba(255,255,255,.75); padding: 3px 0; }
  .cover-band { position: absolute; top: 96px; left: 0; width: 100%; height: 150px; background: linear-gradient(180deg, var(--brand-blue) 0%, var(--brand-blue-deep) 100%); color: #fff; text-align: center; }
  .cover-title { font-family: "Oswald", sans-serif; font-weight: 500; font-size: 60px; line-height: 1; margin-top: 16px; letter-spacing: 1px; }
  .cover-subtitle { font-size: 8.5px; font-weight: 600; line-height: 1.45; margin: 12px 28px 0; text-transform: uppercase; letter-spacing: .4px; }
  .cover-publisher { top: 258px; color: var(--ink); }
  .cover-graphic { position: absolute; left: 0; top: 285px; width: 285px; height: 160px; background: linear-gradient(170deg, #ffffff 0%, #d6edf8 45%, var(--brand-blue-light) 100%); }

  /* Back page */
  .back-surface { position: absolute; inset: 0; background: linear-gradient(150deg, #5ec0eb 0%, var(--brand-blue) 50%, #2593cf 100%); }
  .back-publisher { top: 126px; color: #fff; font-size: 11px; }
  .back-copyright { position: absolute; bottom: 42px; width: 100%; text-align: center; color: #fff; font-size: 6px; letter-spacing: 1px; line-height: 1.6; text-transform: uppercase; }

  /* Preface */
  .preface-photo { position: absolute; inset: 0; background: linear-gradient(180deg, #3b3b3b 0%, #9a9a9a 35%, #6d6d6d 70%, #262626 100%); }
  .preface-panel { position: absolute; left: 42px; top: 82px; width: 200px; height: 270px; background: rgba(255,255,255,.88); padding: 16px; }
  .preface-title { text-align: center; font-family: "Oswald", sans-serif; font-size: 17px; letter-spacing: 2px; color: var(--brand-blue); margin-bottom: 12px; }
  .preface-text { font-size: 6.5px; line-height: 1.65; color: #555; margin-bottom: 8px; }
  .preface-publisher { bottom: 40px; color: #fff; }

  /* Contents */
  .contents-surface { position: absolute; inset: 0; background: linear-gradient(150deg, #5ec0eb 0%, var(--brand-blue) 55%, #2593cf 100%); }
  .contents-panel { position: absolute; left: 36px; top: 58px; width: 213px; height: 265px; background: #fff; border: 4px solid rgba(255,255,255,.55); background-clip: padding-box; }
  .contents-header { background: var(--brand-blue); color: #fff; text-align: center; font-family: "Oswald", sans-serif; font-size: 13px; letter-spacing: 1.5px; padding: 6px 0; margin: 8px 8px 10px; }
  .contents-list { list-style: none; padding: 0 14px; }
  .contents-item { display: flex; align-items: baseline; font-size: 6px; font-weight: 600; color: #555; margin-bottom: 12px; letter-spacing: .3px; }
  .contents-item__dots { flex: 1; border-bottom: 1px dotted var(--brand-gray); margin: 0 4px; }
  .contents-item__num { color: var(--brand-blue); }
  .contents-publisher { bottom: 40px; color: #fff; }
</style>
</head>
<body>

<section class="page page--front">
  <div class="cover-photo" role="img" aria-label="Upward view of glass office towers against a pale sky"></div>
  <p class="cover-kicker">TURNING TRAINING INTO</p>
  <div class="cover-band">
    <h1 class="cover-title">GROWTH 2.0</h1>
    <p class="cover-subtitle">A playbook for launching your revenue generating online professional learning business.</p>
  </div>
  <p class="publisher cover-publisher">Brightlantern Works</p>
  <div class="cover-graphic" role="img" aria-label="Blue three-dimensional rising arrow showing growth"></div>
</section>
<p class="page-label page-label--front">FRONT PAGE</p>

<section class="page page--back">
  <div class="back-surface" role="img" aria-label="Blue faceted geometric background"></div>
  <p class="publisher back-publisher">Brightlantern Works</p>
  <p class="back-copyright">© Copyright 2016 Brightlantern Works<br>All rights reserved</p>
</section>
<p class="page-label page-label--back">BACK PAGE</p>

<section class="page page--preface">
  <div class="preface-photo" role="img" aria-label="Black and white photo of a businessman standing at a large office window"></div>
  <div class="preface-panel">
    <h2 class="preface-title">PREFACE</h2>
    <p class="preface-text">Professional learning has become one of the fastest growing segments of the online education market, and organizations are looking for new ways to reach learners.</p>
    <p class="preface-text">This playbook walks through the steps needed to plan, launch and grow a revenue generating learning business built around certifications and continuing education.</p>
    <p class="preface-text">Use it as a guide to shape your strategy and measure your progress.</p>
  </div>
  <p class="publisher preface-publisher">Brightlantern Works</p>
</section>
<p class="page-label page-label--preface">INNER 1</p>

<section class="page page--contents">
  <div class="contents-surface" role="img" aria-label="Blue faceted geometric background"></div>
  <div class="contents-panel">
    <h2 class="contents-header">TABLE OF CONTENTS</h2>
    <ol class="contents-list">
      <li class="contents-item">UNDERSTANDING THE MARKET OPPORTUNITY<span class="contents-item__dots"></span><span class="contents-item__num">3</span></li>
      <li class="contents-item">THE EVOLUTION OF ONLINE LEARNING<span class="contents-item__dots"></span><span class="contents-item__num">5</span></li>
      <li class="contents-item">THE MODERN LEARNING LANDSCAPE<span class="contents-item__dots"></span><span class="contents-item__num">7</span></li>
      <li class="contents-item">BUILDING YOUR OFFERING<span class="contents-item__dots"></span><span class="contents-item__num">9</span></li>
      <li class="contents-item">PRICING AND PACKAGING<span class="contents-item__dots"></span><span class="contents-item__num">11</span></li>
      <li class="contents-item">MEASURING YOUR RESULTS<span class="contents-item__dots"></span><span class="contents-item__num">13</span></li>
      <li class="contents-item">SCALING YOUR BUSINESS<span class="contents-item__dots"></span><span class="contents-item__num">15</span></li>
      <li class="contents-item">CHOOSING A PLATFORM<span class="contents-item__dots"></span><span class="contents-item__num">17</span></li>
    </ol>
  </div>
  <p class="publisher contents-publisher">Brightlantern Works</p>
</section>
<p class="page-label page-label--contents">INNER 2</p>

</body>
</html>
```